Creative, Striking, Responsive Tutoring Flyer

I need a designer superstar to create an attractive, modern and eye-catching flyer for me. I'm a teacher and I need the flyer to sell French & German private lessons.

Attached is an example that I like a lot. Please create a similar design.

```html
<!DOCTYPE html>
<html lang="en">
<head>
<meta charset="utf-8">
<title>French &amp; German Private Lessons Flyer</title>
<link href="https://fonts.googleapis.com/css2?family=Cabin+Sketch:wght@400;700&family=Kalam:wght@400;700&display=swap" rel="stylesheet">
<style>
  :root {
    --backdrop: #e6e6e6;
    --board-dark: #1c1c1c;
    --board-mid: #2f2f2f;
    --chalk-white: #f4f4f4;
    --chalk-yellow: #f2c414;
    --chalk-orange: #f5871f;
    --supply-pink: #ee3f86;
    --supply-yellow: #f6d23a;
    --supply-purple: #9b6fd8;
    --supply-blue: #43b6e6;
    --supply-green: #27a35a;
  }
  * { margin: 0; padding: 0; box-sizing: border-box; }
  html, body {
    width: 1200px;
    height: 4000px;
    overflow: hidden;
    background: var(--backdrop);
  }
  .flyer {
    position: absolute;
    left: 121px;
    width: 958px;
    height: 1358px;
    overflow: hidden;
    box-shadow: 0 6px 18px rgba(0,0,0,0.25);
  }
  .flyer--front { top: 560px; }
  .flyer--back { top: 2008px; }

  .chalkboard {
    position: absolute;
    inset: 0;
    background: radial-gradient(ellipse at 50% 45%, var(--board-mid) 0%, #262626 55%, var(--board-dark) 100%);
  }
  .supplies {
    position: absolute;
    left: 0;
    width: 100%;
  }
  .supplies--top {
    top: 0;
    height: 250px;
    background: linear-gradient(90deg, var(--supply-pink) 0%, var(--supply-yellow) 25%, var(--supply-purple) 45%, #f3d98a 60%, #f2c6d2 75%, var(--supply-green) 90%, var(--supply-pink) 100%);
    -webkit-mask-image: linear-gradient(180deg, #000 55%, transparent 100%);
            mask-image: linear-gradient(180deg, #000 55%, transparent 100%);
  }
  .supplies--bottom {
    bottom: 0;
    height: 310px;
    background: linear-gradient(90deg, var(--supply-blue) 0%, var(--supply-pink) 25%, var(--supply-purple) 45%, var(--supply-yellow) 62%, #f7b59e 78%, var(--supply-green) 100%);
    -webkit-mask-image: linear-gradient(0deg, #000 55%, transparent 100%);
            mask-image: linear-gradient(0deg, #000 55%, transparent 100%);
  }

  .headline {
    position: absolute;
    left: 0;
    width: 100%;
    text-align: center;
    font-family: "Cabin Sketch", "Georgia", serif;
    font-weight: 700;
    line-height: 1;
    white-space: nowrap;
  }
  .headline--join { top: 390px; font-size: 265px; color: var(--chalk-white); }
  .headline--today { top: 620px; font-size: 170px; color: var(--chalk-yellow); }
  .headline--languages { top: 780px; font-size: 96px; color: var(--chalk-orange); }
  .headline--lessons { top: 870px; font-size: 82px; color: var(--chalk-white); font-weight: 400; }

  .reading-glasses {
    position: absolute;
    left: 610px;
    top: 760px;
    width: 348px;
    height: 280px;
    background: radial-gradient(ellipse at 60% 50%, #3c3c3c 0%, #2b2b2b 55%, rgba(40,40,40,0) 80%);
  }

  .teacher-name {
    position: absolute;
    left: 76px;
    top: 300px;
    font-family: "Cabin Sketch", "Georgia", serif;
    font-weight: 700;
    font-size: 88px;
    line-height: 1;
    color: var(--chalk-white);
  }
  .teacher-name .surname { color: var(--chalk-yellow); }
  .teacher-role {
    position: absolute;
    left: 86px;
    top: 398px;
    font-family: "Kalam", cursive;
    font-weight: 700;
    font-size: 22px;
    color: var(--chalk-orange);
  }

  .contact {
    position: absolute;
    left: 88px;
    display: flex;
    align-items: center;
    gap: 34px;
    font-family: "Kalam", cursive;
    color: var(--chalk-white);
  }
  .contact__icon {
    width: 48px;
    height: 48px;
    flex: none;
    border-radius: 8px;
    background: var(--chalk-orange);
    display: flex;
    align-items: center;
    justify-content: center;
  }
  .contact__icon svg { width: 30px; height: 30px; }
  .contact__text { font-size: 34px; line-height: 1.15; }
  .contact--phone { top: 472px; }
  .contact--phone .contact__text { font-size: 56px; }
  .contact--address { top: 592px; }
  .contact--address .contact__text { font-size: 27px; font-weight: 700; }
  .contact--email { top: 700px; }
  .contact--social { top: 786px; }
  .contact--handle { top: 896px; }
</style>
</head>
<body>

<section class="flyer flyer--front" aria-label="Flyer front">
  <div class="chalkboard" role="img" aria-label="Dark chalkboard texture with white chalk doodles"></div>
  <div class="supplies supplies--top" role="img" aria-label="Photo of school supplies: pink calculator, markers, erasers and spiral notebook"></div>
  <div class="supplies supplies--bottom" role="img" aria-label="Photo of school supplies: pencil case, paper clips, markers, sharpener, crayons and scissors"></div>

  <div class="headline headline--join">JOIN</div>
  <div class="headline headline--today">TODAY</div>
  <div class="headline headline--languages">French &amp; German</div>
  <div class="headline headline--lessons">Private lessons</div>
</section>

<section class="flyer flyer--back" aria-label="Flyer back">
  <div class="chalkboard" role="img" aria-label="Dark chalkboard texture with white chalk doodles"></div>
  <div class="supplies supplies--top" role="img" aria-label="Photo of school supplies: pink calculator, markers, erasers and spiral notebook"></div>
  <div class="supplies supplies--bottom" role="img" aria-label="Photo of school supplies: pencil case, paper clips, markers, sharpener, crayons and scissors"></div>
  <div class="reading-glasses" role="img" aria-label="Photo of black reading glasses on the chalkboard"></div>

  <h1 class="teacher-name">Lena <span class="surname">Moreau</span></h1>
  <p class="teacher-role">French &amp; German Teacher</p>

  <div class="contact contact--phone">
    <span class="contact__icon">
      <svg viewBox="0 0 24 24" aria-hidden="true"><path fill="#fff" d="M6.6 10.8c1.4 2.8 3.8 5.1 6.6 6.6l2.2-2.2c.3-.3.7-.4 1-.2 1.1.4 2.3.6 3.6.6.6 0 1 .4 1 1V20c0 .6-.4 1-1 1C10.6 21 3 13.4 3 4c0-.6.4-1 1-1h3.5c.6 0 1 .4 1 1 0 1.3.2 2.5.6 3.6.1.3 0 .7-.2 1z"/></svg>
    </span>
    <span class="contact__text">(32) 90415 - 2286</span>
  </div>

  <div class="contact contact--address">
    <span class="contact__icon">
      <svg viewBox="0 0 24 24" aria-hidden="true"><path fill="#fff" d="M12 2C8.1 2 5 5.1 5 9c0 5.2 7 13 7 13s7-7.8 7-13c0-3.9-3.1-7-7-7zm0 9.5c-1.4 0-2.5-1.1-2.5-2.5S10.6 6.5 12 6.5s2.5 1.1 2.5 2.5-1.1 2.5-2.5 2.5z"/></svg>
    </span>
    <span class="contact__text">Rua das Acácias, 210/15 - Centro Comercial Jardim Plaza<br>(antiga galeria do mercado)</span>
  </div>

  <div class="contact contact--email">
    <span class="contact__icon">
      <svg viewBox="0 0 24 24" aria-hidden="true"><path fill="#fff" d="M3 5h18c.6 0 1 .4 1 1v12c0 .6-.4 1-1 1H3c-.6 0-1-.4-1-1V6c0-.6.4-1 1-1zm1 2.3V17h16V7.3l-8 5.2-8-5.2zM5.2 7l6.8 4.4L18.8 7H5.2z"/></svg>
    </span>
    <span class="contact__text">aulaslinguasjf@mailbox.com</span>
  </div>

  <div class="contact contact--social">
    <span class="contact__icon"></span>
    <span class="contact__text">social.page/aulaslinguasjf</span>
  </div>

  <div class="contact contact--handle">
    <span class="contact__icon"></span>
    <span class="contact__text">@aulaslinguasjf</span>
  </div>
</section>

</body>
</html>
```